Lantern Advisory
Letterhead design for Marketing Company
Bright & Fun-filled
Nadia Corvane
Inspiration Director
No address needed, please disregard
lanternadvise@mailbrook.net
www.lanternadvisory.ca
Certified QTPR Practitioner B.A. Linguistics
Ask about any of the following services: Corporate workshops Diversity Training Marketing Analysis Career Counseling Entrepreneur Motivation Package QTPR Personality Testing Accent Reduction

```html
<!DOCTYPE html>
<html lang="en">
<head>
<meta charset="utf-8">
<title>Lantern Advisory – Business Card</title>
<link rel="stylesheet" href="https://fonts.googleapis.com/css2?family=Questrial&display=swap">
<style>
  :root {
    --backdrop: #e6e4e1;
    --card-black: #111111;
    --card-white: #ffffff;
    --accent-yellow: #f5c518;
    --ink-dark: #1a1a1a;
    --ink-light: #f2f2f2;
    --ink-muted: #bdbdbd;
  }
  * { margin: 0; padding: 0; box-sizing: border-box; }
  html, body {
    width: 1200px; height: 901px; overflow: hidden;
    background: var(--backdrop);
    font-family: "Questrial", "Century Gothic", sans-serif;
  }
  .stage {
    position: relative; width: 1200px; height: 901px;
    display: flex; align-items: center; justify-content: center; gap: 40px;
  }
  .card {
    position: relative; width: 540px; height: 309px;
    border-radius: 16px; overflow: hidden;
    box-shadow: 0 6px 18px rgba(0,0,0,0.18);
  }

  /* Back side */
  .card-back { background: var(--card-black); color: var(--ink-light); }
  .card-back .brand {
    position: absolute; top: 58px; left: 0; right: 0;
    display: flex; align-items: center; justify-content: center; gap: 10px;
  }
  .brand-dot {
    width: 14px; height: 14px; border-radius: 50%;
    background: var(--accent-yellow);
  }
  .brand-name {
    font-size: 30px; letter-spacing: 1px; line-height: 1;
  }
  .card-back .brand-name { color: var(--ink-light); }
  .service-list {
    position: absolute; top: 118px; left: 0; right: 0;
    list-style: none; text-align: center;
    font-size: 14px; line-height: 19px; color: var(--ink-light);
  }

  /* Front side */
  .card-front { display: flex; background: var(--card-black); }
  .front-brand-panel {
    width: 330px; height: 100%; background: var(--card-white);
    display: flex; align-items: center; justify-content: center; gap: 10px;
  }
  .card-front .brand-name { color: var(--ink-dark); font-size: 32px; }
  .accent-stripe { width: 7px; height: 100%; background: var(--accent-yellow); }
  .contact-panel { flex: 1; padding: 108px 0 0 22px; color: var(--ink-light); }
  .person-name { font-size: 20px; color: var(--accent-yellow); line-height: 1.1; }
  .person-title { font-size: 12px; color: var(--ink-muted); margin-top: 3px; }
  .contact-list { list-style: none; margin-top: 22px; }
  .contact-item {
    display: flex; align-items: center; gap: 8px;
    font-size: 11.5px; line-height: 18px;
  }
  .contact-icon { width: 12px; height: 12px; flex: none; }
</style>
</head>
<body>
<main class="stage">
  <section class="card card-back" aria-label="Card back">
    <div class="brand">
      <span class="brand-dot"></span>
      <span class="brand-name">Lantern Advisory</span>
    </div>
    <ul class="service-list">
      <li>Corporate workshops</li>
      <li>Diversity Training</li>
      <li>Marketing Analysis</li>
      <li>Career Counseling</li>
      <li>Entrepreneur Motivation Package</li>
      <li>QTPR Personality Testing</li>
      <li>Accent Reduction</li>
    </ul>
  </section>

  <section class="card card-front" aria-label="Card front">
    <div class="front-brand-panel">
      <span class="brand-dot"></span>
      <span class="brand-name">Lantern Advisory</span>
    </div>
    <div class="accent-stripe"></div>
    <div class="contact-panel">
      <p class="person-name">Nadia Corvane</p>
      <p class="person-title">Inspiration Director</p>
      <ul class="contact-list">
        <li class="contact-item">
          <svg class="contact-icon" viewBox="0 0 12 12" aria-hidden="true">
            <rect x="3" y="0.5" width="6" height="11" rx="1.2" fill="none" stroke="#f5c518" stroke-width="1.3"/>
            <circle cx="6" cy="9.3" r="0.8" fill="#f5c518"/>
          </svg>
          <span>780-555-0143</span>
        </li>
        <li class="contact-item">
          <svg class="contact-icon" viewBox="0 0 12 12" aria-hidden="true">
            <rect x="0.5" y="2.5" width="11" height="7.5" rx="1" fill="#f5c518"/>
            <path d="M1 3 L6 7 L11 3" fill="none" stroke="#111" stroke-width="1"/>
          </svg>
          <span>lanternadvise@mailbrook.net</span>
        </li>
        <li class="contact-item">
          <svg class="contact-icon" viewBox="0 0 12 12" aria-hidden="true">
            <circle cx="6" cy="6" r="5.3" fill="none" stroke="#f5c518" stroke-width="1.2"/>
            <ellipse cx="6" cy="6" rx="2.3" ry="5.3" fill="none" stroke="#f5c518" stroke-width="1"/>
            <line x1="0.7" y1="6" x2="11.3" y2="6" stroke="#f5c518" stroke-width="1"/>
          </svg>
          <span>www.lanternadvisory.ca</span>
        </li>
      </ul>
    </div>
  </section>
</main>
</body>
</html>
```